Skin Care Package Design

Hello,

I have a unique situation at hand. I already posted a project for this and we chose a winner but we ended up having trademark concerns so we need to modify the designs on the package.

We do not blame the designer in any way and we think that they did an incredible job. We have also chosen him as the winner and paid him so we have full right to share this and have 100% ownership of the design.

Our biggest competitor is Lumo Brisk Dot. We need to be careful not to have a design that is too close to theirs. I think the color red is fine in general, but we need to stay away from any shapes/designs that would be considered similar. They have a partial circle design on the corner and ours is to similar in our opinion - our mistake.

Our name is no longer Velden Face Co. It is now TOLVEN or Tolven.

We need:
1. Velden Face Co removed and "TOLVEN" or "Tolven" put in it's place. You do NOT have to leave the rectangle border. We do not have a design file or the logo yet. We like modern fonts.
2. Please remove the circular designs in the corners. It too closely resembles our competitors package. A square or some other unique concept would work. Feel free to use your imagination. We loved our current design because it's clean and simple but looks good.
3. Please don't mess with the text. We like it and the layout. Our focus is on the color/s and unique design that is going to replace the circle in the corners.
4. Please change "144" in the bottom right to "36".
5. The color red is still fine but we would be curious to see other colors like the green or blue that Dunmel has or maybe a taupe. Use your imagination. We really want colors that pop and grab your attention. Feel free to use more than one color.

I have uploaded two images.
1. Lumo - Is our competitor's package.
2. Velden Face Co is our previous/current package design.

Package deminsions: 5”x3.4”x0.47”

Thanks! Good luck!

Target Market(s)

Male & female. We don't want the package design to be too masculine or too feminine.

Industry/Entity Type

Skin care, health & cosmetics.

Font styles to use
Sans Serif

Requirements
Must have
• You can search acne patch brands on Shopnest and see our competitors. We want ours to look better than Lumo Brisk Dot. They are the top seller. They have a simple and clean design but the red really grabs your eye. There are a ton of brands on the Shopnest page so it's important that the package looks good and the color/s catch your eye.

```html
<!DOCTYPE html>
<html lang="en">
<head>
<meta charset="utf-8">
<title>Tolven – The Acne Patch package front</title>
<link rel="stylesheet" href="https://fonts.googleapis.com/css2?family=Poppins:wght@400;500;600;700&display=swap">
<style>
  :root {
    --backdrop: #939499;
    --card: #ffffff;
    --ink: #151515;
    --ink-soft: #565656;
    --brand-blue: #21399a;
    --acne-blue: #1f3c9c;
    --band-light: #8ec3dc;
    --band-mid: #4aa0cf;
    --band-deep: #3f5fa8;
    --sky: #3ab3f2;
    --ocean: #1a72d6;
  }
  * { margin: 0; padding: 0; box-sizing: border-box; }
  html, body {
    width: 1200px;
    height: 1200px;
    overflow: hidden;
    background: var(--backdrop);
    font-family: "Poppins", sans-serif;
  }
  .package {
    position: absolute;
    left: 315px;
    top: 116px;
    width: 569px;
    height: 968px;
    background: var(--card);
    box-shadow: 6px 8px 14px rgba(0, 0, 0, 0.35);
    overflow: hidden;
  }
  .package-art {
    position: absolute;
    inset: 0;
    width: 569px;
    height: 968px;
  }
  .brand-pill {
    position: absolute;
    left: 61px;
    top: 263px;
    width: 219px;
    height: 40px;
    border-radius: 20px;
    background: var(--brand-blue);
    color: #fff;
    font-weight: 600;
    font-size: 33px;
    line-height: 40px;
    text-align: center;
    letter-spacing: 1px;
  }
  .title-line {
    position: absolute;
    left: 58px;
    font-size: 84px;
    line-height: 1;
    letter-spacing: -1px;
    color: var(--ink);
  }
  .title-the { top: 299px; font-weight: 400; }
  .title-acne { top: 374px; font-weight: 700; color: var(--acne-blue); }
  .title-patch { top: 447px; font-weight: 700; }
  .tagline {
    position: absolute;
    left: 61px;
    top: 563px;
    font-size: 38px;
    line-height: 40px;
    font-weight: 600;
    color: var(--ink-soft);
  }
  .benefit {
    position: absolute;
    left: 61px;
    top: 658px;
    font-size: 18.5px;
    line-height: 24px;
    font-weight: 400;
    color: var(--ink);
  }
  .arc-text {
    font-family: "Poppins", sans-serif;
    font-weight: 600;
    fill: var(--ink);
  }
  .badge-count {
    font-family: "Poppins", sans-serif;
    font-weight: 700;
    font-size: 62px;
    fill: var(--ink);
  }
  .badge-label {
    font-family: "Poppins", sans-serif;
    font-weight: 600;
    font-size: 14px;
    fill: var(--ink);
  }
</style>
</head>
<body>
  <div class="package">
    <svg class="package-art" viewBox="0 0 569 968" xmlns="http://www.w3.org/2000/svg">
      <defs>
        <linearGradient id="topBand" x1="0" y1="0" x2="1" y2="0">
          <stop offset="0" stop-color="var(--band-light)"/>
          <stop offset="0.6" stop-color="var(--band-mid)"/>
          <stop offset="1" stop-color="var(--band-deep)"/>
        </linearGradient>
        <linearGradient id="bottomBand" x1="0" y1="0" x2="1" y2="0">
          <stop offset="0" stop-color="#3bb6f0"/>
          <stop offset="0.6" stop-color="#5db9e8"/>
          <stop offset="1" stop-color="#4463ad"/>
        </linearGradient>
        <linearGradient id="tileFieldTop" x1="0" y1="1" x2="1" y2="0">
          <stop offset="0" stop-color="#ffffff"/>
          <stop offset="0.35" stop-color="#d4e9fb"/>
          <stop offset="0.62" stop-color="var(--sky)"/>
          <stop offset="1" stop-color="var(--ocean)"/>
        </linearGradient>
        <linearGradient id="tileFieldBottom" x1="0" y1="1" x2="1" y2="0">
          <stop offset="0" stop-color="#3a8fe0"/>
          <stop offset="0.45" stop-color="#bcdcf7"/>
          <stop offset="1" stop-color="#ffffff"/>
        </linearGradient>
        <radialGradient id="patchShade" cx="0.35" cy="0.35" r="0.75">
          <stop offset="0" stop-color="#ffffff"/>
          <stop offset="1" stop-color="#c9cbcf"/>
        </radialGradient>
        <path id="stickerTopArc" d="M -89.1 12.5 A 90 90 0 0 1 23.3 -86.9"/>
        <path id="stickerBottomArc" d="M -88.5 61.9 A 108 108 0 1 0 69.4 -82.7"/>
        <path id="badgeTopArc" d="M -71 -2.5 A 71 71 0 0 1 71 -2.5"/>
        <path id="badgeBottomArc" d="M -71.3 49.9 A 87 87 0 0 0 75.3 43.5"/>
      </defs>

      <!-- header band with hang hole -->
      <rect class="header-band" x="0" y="0" width="569" height="104" fill="url(#topBand)"/>
      <g class="hang-hole" fill="#ffffff">
        <rect x="217" y="38" width="134" height="41" rx="20.5"/>
        <ellipse cx="284" cy="40" rx="22" ry="16"/>
      </g>

      <!-- tile field areas -->
      <rect class="tile-field-top" x="55" y="104" width="514" height="373" fill="url(#tileFieldTop)"
            role="img" aria-label="Decorative blue quarter-circle tile pattern"/>
      <rect class="tile-field-bottom" x="0" y="735" width="305" height="183" fill="url(#tileFieldBottom)"
            role="img" aria-label="Decorative blue quarter-circle tile pattern"/>

      <!-- footer band -->
      <rect class="footer-band" x="0" y="918" width="569" height="50" fill="url(#bottomBand)"/>

      <!-- transparent patch seal -->
      <g class="patch-seal" transform="translate(430 224)">
        <circle r="65" fill="url(#patchShade)" role="img" aria-label="Illustration of a peeling transparent patch"/>
        <text class="arc-text" font-size="19" letter-spacing="2">
          <textPath href="#stickerTopArc">TRANSPARENT</textPath>
        </text>
        <text class="arc-text" font-size="19" letter-spacing="4.5">
          <textPath href="#stickerBottomArc">YOUR BELMISH WIZARD</textPath>
        </text>
      </g>

      <!-- count badge -->
      <g class="count-badge" transform="translate(422 822)">
        <text class="arc-text" font-size="18" letter-spacing="2.5">
          <textPath href="#badgeTopArc">8MM &amp; 12MM SIZES</textPath>
        </text>
        <text class="badge-count" x="0" y="18" text-anchor="middle">36</text>
        <text class="badge-label" x="0" y="43" text-anchor="middle">HYDROCOLLOID</text>
        <text class="badge-label" x="0" y="59" text-anchor="middle">PATCHES</text>
        <text class="arc-text" font-size="18" letter-spacing="4">
          <textPath href="#badgeBottomArc">NON-DRYING</textPath>
        </text>
      </g>
    </svg>

    <div class="brand-pill">TOLVEN</div>
    <div class="title-line title-the">THE</div>
    <div class="title-line title-acne">ACNE</div>
    <div class="title-line title-patch">PATCH</div>
    <p class="tagline">Ideal for<br>surface spots</p>
    <p class="benefit">Gently absorbs gunk in 6-8 hours<br>&amp; approves the look of pimples<br>overnight.</p>
  </div>
</body>
</html>
```